Dalvor Inc Business Card

Looking to get an updated business card for a Contract Machining company (www.dalvorinc-example.com) - looking for a clean design the portrays the technical nature of the business - colors can follow the website design and be in any combination that makes sense (red black, white, metallic or silver) - logos attached for use also. Would like space for: Name, title, business phone (555 214-3098), cell phone , website (www.dalvorinc-example.com) - possibly QR code could be integrated for website (designer choice), business address - 418 Birchfield Lane, Alder Falls, MI 49921 (cards will be for 4 employees, I will either need to modify a template or I can provide individual information)
Target Market(s)
Aerospace, defense and medical device manufacturing companies that need machining
Industry/Entity Type
Machining for aerospace, defense, medical
Contact Information for Business Card
Name, Title, Business Phone, Cell Phone, email, business website and business address

```html
<!DOCTYPE html>
<html lang="en">
<head>
<meta charset="UTF-8">
<title>Dalvor Inc Business Card</title>
<link rel="stylesheet" href="https://fonts.googleapis.com/css2?family=Montserrat:wght@400;500;700;800&display=swap">
<style>
  :root {
    --stage: #5f7862;
    --card-white: #ffffff;
    --card-black: #060608;
    --brand-red: #b21e24;
    --ink: #111111;
  }
  * { margin: 0; padding: 0; box-sizing: border-box; }
  html, body {
    width: 1200px;
    height: 800px;
    overflow: hidden;
    background: var(--stage);
    font-family: "Montserrat", sans-serif;
  }
  .stage {
    width: 1200px;
    height: 800px;
    display: flex;
    align-items: center;
    justify-content: center;
    gap: 56px;
  }
  .card {
    position: relative;
    width: 520px;
    height: 297px;
    overflow: hidden;
    box-shadow: 0 6px 18px rgba(0,0,0,0.25);
  }
  .card-front { background: var(--card-white); }
  .card-back { background: var(--card-black); }

  .front-accent {
    position: absolute;
    top: 0; right: 0;
    width: 200px;
    height: 297px;
  }
  .company-name {
    position: absolute;
    left: 34px;
    top: 34px;
    font-weight: 800;
    font-size: 28px;
    letter-spacing: 0.5px;
    color: var(--brand-red);
    text-transform: uppercase;
  }
  .person {
    position: absolute;
    left: 34px;
    top: 140px;
  }
  .person-name {
    font-weight: 700;
    font-size: 22px;
    color: var(--ink);
    line-height: 1.1;
  }
  .person-title {
    font-weight: 700;
    font-size: 13px;
    color: var(--brand-red);
    margin-top: 2px;
  }
  .contact {
    position: absolute;
    left: 34px;
    top: 210px;
    font-size: 11.5px;
    font-weight: 500;
    font-style: normal;
    color: var(--ink);
    line-height: 1.6;
  }

  .back-brand {
    position: absolute;
    inset: 0;
    display: flex;
    flex-direction: column;
    align-items: center;
    justify-content: center;
    gap: 14px;
  }
  .back-brand-dot {
    width: 110px;
    height: 110px;
    border-radius: 50%;
    background: var(--brand-red);
  }
  .back-brand-name {
    font-weight: 800;
    font-size: 26px;
    letter-spacing: 0.5px;
    color: var(--brand-red);
    text-transform: uppercase;
  }
</style>
</head>
<body>
  <main class="stage">
    <section class="card card-front" aria-label="Business card front">
      <svg class="front-accent" viewBox="0 0 200 297" aria-hidden="true">
        <polygon points="40,0 200,0 200,297 150,297" fill="var(--brand-red)"/>
        <polygon points="200,150 200,297 120,297" fill="var(--card-black)"/>
      </svg>
      <div class="company-name">Dalvor Inc</div>
      <div class="person">
        <div class="person-name">Owner Name</div>
        <div class="person-title">CEO</div>
      </div>
      <address class="contact">
        <div>418 Birchfield Lane, Alder Falls, MI 49921</div>
        <div>Phone: 555 214-3098 | Cell: 555 214-3098</div>
        <div>www.dalvorinc-example.com</div>
      </address>
    </section>

    <section class="card card-back" aria-label="Business card back">
      <div class="back-brand">
        <div class="back-brand-dot"></div>
        <div class="back-brand-name">Dalvor Inc</div>
      </div>
    </section>
  </main>
</body>
</html>
```